Create a new website for "The Arcade at Fernbrook"

I need a website for a shopping center in Atlanta USA. I want a classy high end look with high end motion videos (which I will provide).
The purpose of website is to attract new tenants to fill up vacant office spaces we have.
we will highlight existing cool stores and advertise that this is a cool place to start a new tenants business or office . ideally IT businesses in Alpharetta city in Georgia state in USA

Target Market(s)

commercial office tenants

Industry/Entity Type

Real Estate

Contact Information for Business Card

classy high end design
Arcade at Fernbrook
address:
2870 Briarwell Pkwy
Alpharetta GA 30005

Logo Text

I am open. Anything that attracts new IT tech tenants to lease up shopping center/ office space

Coding

Coded - Design and coding required

Number of Pages Required

5+ page

Requirements
Must have
• easy to browse

here is a link to some photos. i will provide videos shortly

http://www.tomsereph.com/2014/04/Building-Photos-3/n-5N2dg/
Nice to have
• please look at some of mall websites i like. Moving videos and images on home page

I really like this one: https://www.plazaatcresthollow.com/

others are

https://lindorecenter.com/

https://www.discoverbrisket.com/

```html
<!DOCTYPE html>
<html lang="en">
<head>
<meta charset="utf-8">
<title>The Arcade at Fernbrook</title>
<link href="https://fonts.googleapis.com/css2?family=Playfair+Display:wght@400;700;900&family=Montserrat:wght@400;500;600;700&display=swap" rel="stylesheet">
<style>
:root{
  --ink:#111111;
  --black:#0b0b0b;
  --white:#ffffff;
  --mist:#e9e9e9;
  --grey:#8a8a8a;
  --soft:#cfcfcf;
  --night:#0d1420;
}
*{box-sizing:border-box;margin:0;padding:0}
html,body{width:1200px;height:3884px;overflow:hidden}
body{background:var(--white);color:var(--ink);font-family:"Montserrat",sans-serif;position:relative}
.serif{font-family:"Playfair Display",serif}
.photo{display:block}

/* nav */
.site-nav{position:absolute;top:0;left:0;width:1200px;height:64px;background:#2a2a2a;display:flex;align-items:center;justify-content:space-between;padding:0 92px}
.brand{font-family:"Playfair Display",serif;color:var(--white);font-size:22px;font-weight:700}
.menu{display:flex;gap:40px;list-style:none}
.menu li{color:var(--white);font-size:14px;font-weight:500;position:relative}
.menu li.active::after{content:"";position:absolute;left:0;right:0;bottom:-8px;height:2px;background:var(--white)}

/* hero */
.hero{position:absolute;top:64px;left:0;width:1200px;height:576px;background:linear-gradient(180deg,#d9dde2 0%,#c7cdd3 45%,#8d8a84 75%,#4d4a46 100%)}
.hero-title{position:absolute;top:210px;left:0;width:1200px;text-align:center;color:var(--white);font-family:"Playfair Display",serif}
.hero-title .kicker{display:block;font-size:40px;font-weight:700;line-height:1}
.hero-title .city{display:block;font-size:104px;font-weight:700;line-height:1.05}
.hero-arrows{position:absolute;right:100px;bottom:42px;display:flex;gap:6px}
.arrow-btn{width:36px;height:28px;background:rgba(20,20,20,.85);display:flex;align-items:center;justify-content:center}

/* headings */
.section-title{position:absolute;left:0;width:1200px;text-align:center;font-family:"Playfair Display",serif;font-weight:700;font-size:40px;color:var(--ink)}

/* store */
.store-card{position:absolute;top:752px;width:328px}
.store-card .photo{width:328px;height:220px}
.store-card .caption{display:flex;justify-content:space-between;align-items:baseline;margin-top:18px}
.store-card .name{font-family:"Playfair Display",serif;font-size:22px}
.store-card .more{font-size:11px;color:#444}
.store-arrows{position:absolute;top:1040px;left:1044px;display:flex}
.store-arrows span{width:32px;height:28px;border:1px solid var(--ink);display:flex;align-items:center;justify-content:center}
.store-arrows span.dark{background:var(--ink)}

/* about */
.about-band{position:absolute;top:1084px;left:0;width:1200px;height:448px;background:linear-gradient(180deg,#b9cde3 0%,#dfe4e8 40%,#cfc8bc 62%,#7d8a6a 78%,#5a5a58 100%)}
.about-box{position:absolute;top:1132px;left:788px;width:320px;height:348px;background:var(--black);color:var(--white);padding:36px 28px}
.about-box .label{font-family:"Playfair Display",serif;font-size:18px;font-weight:700}
.about-box h2{font-family:"Playfair Display",serif;font-size:36px;line-height:1.1;margin-top:6px}
.about-box p{font-size:11px;line-height:1.6;margin-top:16px;color:#e6e6e6}
.btn-light{display:inline-block;margin-top:22px;background:var(--white);color:var(--ink);font-size:10px;font-weight:700;letter-spacing:2px;padding:10px 22px}

/* blog */
.blog-item{position:absolute;top:1644px;width:328px}
.blog-item .photo{width:328px;height:328px}
.blog-card{position:absolute;top:288px;left:34px;width:260px;height:220px;background:var(--black);color:var(--white);text-align:center;padding:8px}
.blog-card .frame{border:1px solid #fff;height:100%;padding:20px 18px}
.blog-card .date{font-size:11px;font-weight:600}
.blog-card h3{font-family:"Playfair Display",serif;font-size:19px;margin-top:10px}
.blog-card p{font-size:11px;line-height:1.6;margin-top:10px;color:#e3e3e3}
.blog-card .read{font-size:10px;font-weight:700;letter-spacing:2px;margin-top:14px}
.btn-outline{position:absolute;top:2188px;left:520px;width:160px;height:36px;border:1.5px solid var(--ink);font-size:10px;font-weight:700;letter-spacing:2px;display:flex;align-items:center;justify-content:center}

/* newsletter */
.newsletter{position:absolute;top:2288px;left:0;width:1200px;height:352px;background:linear-gradient(180deg,#05080e 0%,#0f1826 45%,#2b2a2a 80%,#151515 100%)}
.newsletter h2{position:absolute;top:96px;width:1200px;text-align:center;color:var(--white);font-family:"Playfair Display",serif;font-size:40px;font-weight:700}
.form{position:absolute;top:164px;left:320px;width:560px}
.form .row{display:flex;gap:8px;margin-bottom:8px}
.field{flex:1;height:32px;background:var(--white);font-size:10px;color:#666;padding:0 10px;display:flex;align-items:center}
.submit{margin-left:210px;width:112px;height:32px;background:var(--white);font-size:10px;font-weight:700;letter-spacing:2px;display:flex;align-items:center;justify-content:center;margin-top:14px}

/* social */
.insta-tile{position:absolute;top:2804px;width:240px;height:304px}
.insta-overlay{position:absolute;inset:20px;background:rgba(0,0,0,.55);border:1px solid rgba(255,255,255,.8);display:flex;align-items:center;justify-content:center;color:var(--white);font-size:12px;font-weight:600}

/* partners */
.partners{position:absolute;top:3160px;left:0;width:1200px;height:352px;background:var(--mist)}
.partner{position:absolute;width:90px;height:90px;display:flex;flex-direction:column;align-items:center;gap:12px}
.partner .mark{width:56px;height:56px;background:#b5b5b5}
.partner .mark.round{border-radius:50%}
.partner .bar{width:60px;height:8px;background:#9d9d9d}

/* footer */
.site-footer{position:absolute;top:3512px;left:0;width:1200px;height:372px;background:var(--black);color:var(--white)}
.col{position:absolute;top:64px}
.col h4{font-size:14px;font-weight:700;margin-bottom:22px}
.col h4.brandline{font-family:"Playfair Display",serif;font-size:20px}
.col p{font-size:11px;line-height:1.7;color:#cfcfcf}
.col ul{list-style:none}
.col li{font-size:11px;color:#cfcfcf;margin-bottom:18px;display:flex;align-items:center;gap:12px}
.dot{width:8px;height:8px;background:#cfcfcf;border-radius:50%}
.copyright{position:absolute;bottom:0;left:0;width:1200px;height:68px;border-top:1px solid #333;display:flex;align-items:center;justify-content:center;font-size:11px;color:#bdbdbd}
</style>
</head>
<body>

<header class="site-nav">
  <div class="brand">The Arcade at Fernbrook</div>
  <ul class="menu">
    <li class="active">Home</li><li>About</li><li>Shop</li><li>Blog</li><li>Contact</li>
  </ul>
</header>

<section class="hero" role="img" aria-label="Shopping center storefront with a white tower entrance under a pale sky">
  <h1 class="hero-title"><span class="kicker">Shopping Center in</span><span class="city">Atlanta USA</span></h1>
  <div class="hero-arrows">
    <span class="arrow-btn"><svg width="12" height="12" viewBox="0 0 12 12"><path d="M8 1 3 6l5 5" stroke="#fff" stroke-width="1.6" fill="none"/></svg></span>
    <span class="arrow-btn"><svg width="12" height="12" viewBox="0 0 12 12"><path d="M4 1l5 5-5 5" stroke="#fff" stroke-width="1.6" fill="none"/></svg></span>
  </div>
</section>

<h2 class="section-title" style="top:676px">Our Store</h2>

<article class="store-card" style="left:92px">
  <div class="photo" style="background:linear-gradient(180deg,#9fc3ea 0%,#d9d2c4 45%,#a9a39a 100%)" role="img" aria-label="Covered walkway along the shopping center storefronts"></div>
  <div class="caption"><span class="name">Lorem ipsum dolor</span><span class="more">View Details &rsaquo;</span></div>
</article>
<article class="store-card" style="left:436px">
  <div class="photo" style="background:linear-gradient(180deg,#5f95d4 0%,#c9c3b6 50%,#8c8780 100%)" role="img" aria-label="Row of shops with a columned facade"></div>
  <div class="caption"><span class="name">Cras sed congue</span><span class="more">View Details &rsaquo;</span></div>
</article>
<article class="store-card" style="left:780px">
  <div class="photo" style="background:linear-gradient(180deg,#4f8dd6 0%,#e3e1dc 50%,#7d7b78 100%)" role="img" aria-label="Shopping center building seen across the parking lot"></div>
  <div class="caption"><span class="name">Morbi Sollicitudin</span><span class="more">View Details &rsaquo;</span></div>
</article>
<div class="store-arrows">
  <span><svg width="10" height="10" viewBox="0 0 10 10"><path d="M7 1 3 5l4 4" stroke="#111" stroke-width="1.5" fill="none"/></svg></span>
  <span class="dark"><svg width="10" height="10" viewBox="0 0 10 10"><path d="M3 1l4 4-4 4" stroke="#fff" stroke-width="1.5" fill="none"/></svg></span>
</div>

<section class="about-band" role="img" aria-label="Wide view of the shopping center with trees and parked cars"></section>
<div class="about-box">
  <div class="label">About</div>
  <h2>The Arcade at Fernbrook</h2>
  <p>Cras sed congue diam. Nulla rutrum enim id ligula aliquam porttitor. Nam ipsum nisi, feugiat eget efficitur nec, mattis euismod blandit risus. Aliquam arcu, curabitur nulla convallis quam.</p>
  <span class="btn-light">READ MORE</span>
</div>

<h2 class="section-title" style="top:1580px">Our Blog</h2>

<article class="blog-item" style="left:92px">
  <div class="photo" style="background:linear-gradient(180deg,#e0a23a 0%,#efe6d6 45%,#b79a74 100%)" role="img" aria-label="Empty bright office interior with glass walls"></div>
  <div class="blog-card"><div class="frame"><div class="date">March 14, 2021</div><h3>Nunc a nunc efficitur</h3><p>Cras sed congue diam. Nulla rutrum enim id ligula aliquam porttitor.</p><div class="read">READ MORE</div></div></div>
</article>
<article class="blog-item" style="left:436px">
  <div class="photo" style="background:linear-gradient(180deg,#d8d8d8 0%,#f4f4f4 40%,#a8a49e 100%)" role="img" aria-label="Atrium interior with skylight and railings"></div>
  <div class="blog-card"><div class="frame"><div class="date">March 14, 2021</div><h3>Nunc a nunc efficitur</h3><p>Cras sed congue diam. Nulla rutrum enim id ligula aliquam porttitor.</p><div class="read">READ MORE</div></div></div>
</article>
<article class="blog-item" style="left:780px">
  <div class="photo" style="background:linear-gradient(180deg,#6aa0dc 0%,#dcd8cf 50%,#8a8782 100%)" role="img" aria-label="White clock tower of the shopping center"></div>
  <div class="blog-card"><div class="frame"><div class="date">March 14, 2021</div><h3>Nunc a nunc efficitur</h3><p>Cras sed congue diam. Nulla rutrum enim id ligula aliquam porttitor.</p><div class="read">READ MORE</div></div></div>
</article>
<div class="btn-outline">VIEW ALL BLOGS</div>

<section class="newsletter" role="img" aria-label="Shopping center lit up at night">
  <h2>Signup For Newsletter</h2>
  <div class="form">
    <div class="row"><span class="field">First Name</span><span class="field">Last Name</span></div>
    <div class="row"><span class="field">Email Address</span></div>
    <div class="submit">SUBMIT</div>
  </div>
</section>

<h2 class="section-title" style="top:2732px">Follow Us On Snapgrid</h2>
<div class="insta-tile" style="left:92px;background:linear-gradient(180deg,#9cc2e8 0%,#c9c6bf 45%,#6f6d6a 100%)" role="img" aria-label="Parking lot beside the shopping center"></div>
<div class="insta-tile" style="left:352px;background:linear-gradient(180deg,#5a4a40 0%,#a0452f 50%,#d9cdbd 100%)" role="img" aria-label="Vacant retail interior with red walls"></div>
<div class="insta-tile" style="left:612px;background:linear-gradient(180deg,#3a3330 0%,#6b5a52 50%,#2a2624 100%)" role="img" aria-label="Dark interior corridor">
  <div class="insta-overlay">Follow Us</div>
</div>
<div class="insta-tile" style="left:868px;background:linear-gradient(180deg,#7fb0e2 0%,#d4cfc6 50%,#8a847b 100%)" role="img" aria-label="Covered stairway outside the shops"></div>

<section class="partners" aria-label="Partner brands">
  <div class="partner" style="left:92px;top:60px"><span class="mark"></span><span class="bar"></span></div>
  <div class="partner" style="left:275px;top:60px"><span class="mark round"></span><span class="bar"></span></div>
  <div class="partner" style="left:458px;top:60px"><span class="mark"></span><span class="bar"></span></div>
  <div class="partner" style="left:641px;top:60px"><span class="mark round"></span><span class="bar"></span></div>
  <div class="partner" style="left:824px;top:60px"><span class="mark"></span><span class="bar"></span></div>
  <div class="partner" style="left:1010px;top:60px"><span class="mark round"></span><span class="bar"></span></div>
  <div class="partner" style="left:92px;top:200px"><span class="mark round"></span><span class="bar"></span></div>
  <div class="partner" style="left:275px;top:200px"><span class="mark"></span><span class="bar"></span></div>
  <div class="partner" style="left:458px;top:200px"><span class="mark round"></span><span class="bar"></span></div>
  <div class="partner" style="left:641px;top:200px"><span class="mark"></span><span class="bar"></span></div>
  <div class="partner" style="left:824px;top:200px"><span class="mark round"></span><span class="bar"></span></div>
  <div class="partner" style="left:1010px;top:200px"><span class="mark"></span><span class="bar"></span></div>
</section>

<footer class="site-footer">
  <div class="col" style="left:92px;width:300px">
    <h4 class="brandline">The Arcade at Fernbrook</h4>
    <p>Lorem ipsum dolor sit amet, consectetur adipiscing elit. Praesent bibendum, arcu eleifend suscipit gravida, enim augue dapibus odio, at porta felis lectus sit amet risus.</p>
  </div>
  <div class="col" style="left:464px">
    <h4>Quick Links</h4>
    <ul><li>Home</li><li>About</li><li>Shop</li><li>Blog</li><li>Contact</li></ul>
  </div>
  <div class="col" style="left:684px">
    <h4>Follow Us</h4>
    <ul><li><span class="dot"></span>Friendwall</li><li><span class="dot"></span>Chirper</li><li><span class="dot"></span>Snapgrid</li><li><span class="dot"></span>Viewtube</li></ul>
  </div>
  <div class="col" style="left:896px">
    <h4>Contact Us</h4>
    <ul>
      <li><svg width="10" height="12" viewBox="0 0 10 12"><path d="M5 11S1 6.5 1 4a4 4 0 0 1 8 0c0 2.5-4 7-4 7z" fill="#cfcfcf"/></svg>2870 Briarwell Pkwy<br>Alpharetta GA 30005</li>
      <li><svg width="12" height="10" viewBox="0 0 12 10"><rect x="0.5" y="0.5" width="11" height="9" fill="none" stroke="#cfcfcf"/><path d="M1 1l5 4 5-4" fill="none" stroke="#cfcfcf"/></svg>info@arcadeatfernbrook.com</li>
      <li><svg width="11" height="11" viewBox="0 0 11 11"><path d="M2 1h2l1 2.5-1.3 1a6 6 0 0 0 2.8 2.8l1-1.3L10 7v2a1 1 0 0 1-1 1A8 8 0 0 1 1 2a1 1 0 0 1 1-1z" fill="#cfcfcf"/></svg>(770) 555-0148</li>
    </ul>
  </div>
  <div class="copyright">&copy; 2021 The Arcade at Fernbrook. All Rights Reserved.</div>
</footer>

</body>
</html>
```